Business Card Design For DJ Company

I'm rebranding my wedding and event dj company. I am looking for a modern, luxury, & fun design to match my new logo and website design. Please see attached logo and new webpage design. Colors should match. Design should flow with logo and website for recognition. I want to attract young adults. I plan on printing metallic finish cards so please keep hat in mind.

Target Market(s)

Millennials

Contact Information for Business Card

Name: Dario Colvento
Company: Cedar Hollow Mix DJ
Services: DJ – Photo Booth – Event Lighting – LED Robot

Website: www.cedarhollowmixdj.example
Email: dario@cedarhollowmixdj.example
Phone: (555)417-9382

Instagram: @chmixdj
Facebook: @chmixdj
Twitter - @chmixdj

Se Habla Español

Font styles to use
Serif
Sans Serif

Colors

Designer to choose colors to be used in the design.

Requirements
Nice to have
• Transparent Gradient background - Image related to weddings

```html
<!DOCTYPE html>
<html lang="en">
<head>
<meta charset="utf-8">
<title>Cedar Hollow Mix DJ – Business Card</title>
<link rel="stylesheet" href="https://fonts.googleapis.com/css2?family=Arimo:wght@400;700&display=swap">
<style>
  :root {
    --canvas: #ece8e2;
    --card: #fdfdfc;
    --green: #8cc63f;
    --orange: #f7941d;
    --blue: #29abe2;
    --grey: #58595b;
    --sun: #fbe4d5;
    --palm: #e6efdc;
  }
  * { box-sizing: border-box; margin: 0; padding: 0; }
  html, body { width: 1200px; height: 886px; overflow: hidden; }
  body {
    background: var(--canvas);
    font-family: "Arimo", Arial, sans-serif;
    display: flex;
    align-items: center;
    justify-content: center;
    gap: 40px;
  }
  .card {
    position: relative;
    width: 540px;
    height: 309px;
    background: var(--card);
    border-radius: 16px;
    overflow: hidden;
    box-shadow: 0 6px 18px rgba(0,0,0,0.12);
  }

  /* Front */
  .sun {
    position: absolute;
    left: 300px; top: -40px;
    width: 120px; height: 120px;
    border-radius: 50%;
    background: var(--sun);
  }
  .palm-decoration {
    position: absolute;
    left: 20px; top: 30px;
    width: 330px; height: 250px;
    border-radius: 45% 55% 40% 50%;
    background: radial-gradient(ellipse at center, var(--palm) 0%, rgba(230,239,220,0.5) 55%, rgba(230,239,220,0) 75%);
  }
  .contact {
    position: absolute;
    left: 90px; top: 56px;
    width: 250px;
    text-align: center;
  }
  .contact .name {
    color: var(--green);
    font-size: 20px;
    font-weight: 700;
    letter-spacing: 0.5px;
    text-transform: uppercase;
  }
  .contact .divider {
    width: 40px; height: 1px;
    background: var(--grey);
    margin: 9px auto 8px;
  }
  .contact .line {
    color: var(--grey);
    font-size: 12px;
    line-height: 17px;
  }
  .contact .spanish {
    color: var(--orange);
    font-size: 19px;
    font-weight: 700;
    margin-top: 8px;
  }
  .contact .social {
    display: flex;
    justify-content: center;
    align-items: center;
    gap: 5px;
    margin-top: 6px;
    color: var(--blue);
    font-size: 11px;
  }
  .contact .social .dot {
    width: 10px; height: 10px;
    border-radius: 50%;
    background: var(--blue);
  }
  .equalizer {
    position: absolute;
    left: 0; bottom: 0;
    width: 540px; height: 150px;
  }
  .equalizer rect { fill: var(--orange); }

  /* Back */
  .brand {
    position: absolute;
    left: 0; right: 0; top: 78px;
    display: flex;
    justify-content: center;
    align-items: center;
    gap: 12px;
  }
  .brand .mark {
    width: 46px; height: 46px;
    border-radius: 50%;
    background: var(--blue);
  }
  .brand .wordmark {
    color: var(--orange);
    font-size: 30px;
    font-weight: 700;
    text-transform: uppercase;
    letter-spacing: 1px;
  }
  .back-details {
    position: absolute;
    left: 0; right: 0; top: 190px;
    text-align: center;
    color: var(--grey);
  }
  .back-details .handle {
    font-size: 13px;
    display: inline-flex;
    align-items: center;
    gap: 6px;
  }
  .back-details .handle .dot {
    width: 10px; height: 10px;
    border-radius: 50%;
    background: var(--green);
  }
  .back-details .rule {
    width: 220px; height: 1px;
    background: var(--grey);
    margin: 8px auto;
  }
  .back-details .services {
    font-size: 12px;
  }
</style>
</head>
<body>

  <section class="card card-front">
    <div class="sun"></div>
    <div class="palm-decoration" role="img" aria-label="Faint palm tree illustration in pale green"></div>

    <div class="contact">
      <p class="name">Dario Colvento</p>
      <div class="divider"></div>
      <p class="line">(555)417-9382</p>
      <p class="line">dario@cedarhollowmixdj.example</p>
      <p class="line">www.cedarhollowmixdj.example</p>
      <p class="spanish">Se Habla Español</p>
      <p class="social"><span class="dot"></span>@chmixdj</p>
    </div>

    <svg class="equalizer" viewBox="0 0 540 150" aria-hidden="true">
      <rect x="4" y="112" width="6" height="38"/><rect x="15" y="104" width="6" height="46"/>
      <rect x="26" y="120" width="6" height="30"/><rect x="37" y="98" width="6" height="52"/>
      <rect x="48" y="106" width="6" height="44"/><rect x="59" y="114" width="6" height="36"/>
      <rect x="70" y="92" width="6" height="58"/><rect x="81" y="102" width="6" height="48"/>
      <rect x="92" y="110" width="6" height="40"/><rect x="103" y="88" width="6" height="62"/>
      <rect x="114" y="100" width="6" height="50"/><rect x="125" y="80" width="6" height="70"/>
      <rect x="136" y="94" width="6" height="56"/><rect x="147" y="86" width="6" height="64"/>
      <rect x="158" y="72" width="6" height="78"/><rect x="169" y="90" width="6" height="60"/>
      <rect x="180" y="78" width="6" height="72"/><rect x="191" y="66" width="6" height="84"/>
      <rect x="202" y="84" width="6" height="66"/><rect x="213" y="60" width="6" height="90"/>
      <rect x="224" y="76" width="6" height="74"/><rect x="235" y="54" width="6" height="96"/>
      <rect x="246" y="70" width="6" height="80"/><rect x="257" y="48" width="6" height="102"/>
      <rect x="268" y="62" width="6" height="88"/><rect x="279" y="56" width="6" height="94"/>
      <rect x="290" y="42" width="6" height="108"/><rect x="301" y="74" width="6" height="76"/>
      <rect x="312" y="52" width="6" height="98"/><rect x="323" y="38" width="6" height="112"/>
      <rect x="334" y="64" width="6" height="86"/><rect x="345" y="46" width="6" height="104"/>
      <rect x="356" y="32" width="6" height="118"/><rect x="367" y="58" width="6" height="92"/>
      <rect x="378" y="40" width="6" height="110"/><rect x="389" y="26" width="6" height="124"/>
      <rect x="400" y="50" width="6" height="100"/><rect x="411" y="34" width="6" height="116"/>
      <rect x="422" y="20" width="6" height="130"/><rect x="433" y="44" width="6" height="106"/>
      <rect x="444" y="28" width="6" height="122"/><rect x="455" y="14" width="6" height="136"/>
      <rect x="466" y="36" width="6" height="114"/><rect x="477" y="22" width="6" height="128"/>
      <rect x="488" y="10" width="6" height="140"/><rect x="499" y="32" width="6" height="118"/>
      <rect x="510" y="18" width="6" height="132"/><rect x="521" y="4" width="6" height="146"/>
      <rect x="532" y="26" width="6" height="124"/>
    </svg>
  </section>

  <section class="card card-back">
    <div class="brand">
      <span class="mark"></span>
      <span class="wordmark">Cedar Hollow Mix DJ</span>
    </div>
    <div class="back-details">
      <p class="handle"><span class="dot"></span>@chmixdj</p>
      <div class="rule"></div>
      <p class="services">DJ – Photo Booth – Event Lighting – LED Robot</p>
    </div>
  </section>

</body>
</html>
```